Visual design for database driven web application

Need a clean, professional looking visual design for a web application.

PLUME is the new standardized K-12 school testing program for the state of Texas. We are building an application named PLUME-Finder (clever, yeah?) that will allow teachers, school administrators, and others to EASILY sort through millions of records of student data and print or export reports showing just the information they need about their students.

The state currently doesn't provide a user-friendly way to do this. They provide a "data dump" spreadsheet that school administrators and teachers must figure out how to manipulate to get the data they need. We are building a Web-based tool that will make it super simple and easy for our users to get the data they need in a format that works for them.

I've created a basic wireframe of the main application screen in Vellum QD Max. I need you to "skin" the wireframe to make it look good. Your mockup will set the tone for branding and visual design throughout the site.

See the attached screenshots. There are a few variations of the screen that include dynamic panels that open & close. Start by designing just the main screen and if you have time, do one or two of the panels. Thanks!
Updates

Target Market(s)

K-12 education professionals (teachers, administrators) in the state of Texas

Industry/Entity Type

Building

Requirements
Must have
• Your mockups should include all of the features & content shown in the attached screenshots.

However, you don't have to show all 10 rows of data. You can just do the column headers and one row of data. (It would be repetitive and unnecessary to spend time re-creating the entire grid with all of that data just to show your visual styling.)

The design should reflect the following concepts:

- Texas
- Education
- Simplicity
- Helpfulness
- Trust
- Professionalism

If I select your design, I will want your design source files (Illustrator, Photoshop, etc.)
Nice to have
• A logo in the upper left corner for PLUME-Finder. The logo should definitely communicate the design concepts described under "must have."

```html
<!DOCTYPE html>
<html lang="en">
<head>
<meta charset="utf-8">
<title>PLUME-Finder · Student Data</title>
<link rel="stylesheet" href="https://fonts.googleapis.com/css2?family=Open+Sans:wght@400;600;700&display=swap">
<style>
  :root {
    --page-bg: #d6d6d6;
    --bar-dark: #2b2b2b;
    --bar-dark-2: #1c1c1c;
    --nav-top: #f4f4f4;
    --nav-bottom: #dcdcdc;
    --tab-active: #f7f7f7;
    --text: #4a4a4a;
    --text-soft: #6e6e6e;
    --text-light: #e6e6e6;
    --text-dim: #9a9a9a;
    --row-top: #ffffff;
    --row-bottom: #e6e6e6;
    --line: #c9c9c9;
  }
  * { box-sizing: border-box; margin: 0; padding: 0; }
  html, body { width: 1200px; height: 704px; overflow: hidden; }
  body {
    background: var(--page-bg);
    font-family: "Open Sans", Arial, sans-serif;
    color: var(--text);
    position: relative;
  }
  .app { position: absolute; left: 44px; top: 0; width: 1112px; }

  .masthead {
    height: 51px;
    background: linear-gradient(var(--bar-dark), var(--bar-dark-2));
    display: flex; align-items: center; padding: 0 12px 0 18px;
  }
  .brand { display: flex; align-items: center; gap: 10px; color: #f0f0f0; font-size: 26px; font-weight: 400; letter-spacing: 1px; }
  .brand-mark { width: 22px; height: 22px; background: #8a8a8a; }
  .search { margin-left: auto; display: flex; align-items: center; }
  .search-field {
    width: 146px; height: 24px; border-radius: 12px 0 0 12px; background: #f5f5f5;
    font-size: 11px; color: #999; padding: 4px 12px; border: 0;
  }
  .search-btn {
    width: 26px; height: 24px; background: #6b6b6b; border-radius: 0 5px 5px 0;
    display: flex; align-items: center; justify-content: center;
  }
  .search-options { margin-left: 14px; font-size: 11px; color: #ddd; display: flex; align-items: center; gap: 6px; }
  .search-options .chev { width: 14px; height: 14px; background: #eee; border-radius: 2px; display: flex; align-items: center; justify-content: center; }

  .navbar {
    height: 78px; background: linear-gradient(var(--nav-top), var(--nav-bottom));
    display: flex; align-items: stretch; border-left: 1px solid #ccc; border-right: 1px solid #ccc;
  }
  .tab { padding: 0 16px; display: flex; align-items: center; font-size: 12.5px; color: var(--text); }
  .tab.active { background: var(--tab-active); border-left: 1px solid #c8c8c8; border-right: 1px solid #c8c8c8; padding: 0 14px; }
  .user { margin-left: auto; display: flex; align-items: center; gap: 8px; padding-right: 40px; font-size: 12.5px; color: var(--text); }
  .user a { color: var(--text); text-decoration: underline; }
  .user .sep { color: #aaa; }

  .toolbar {
    height: 32px; background: linear-gradient(#3a3a3a, #252525);
    display: flex; align-items: center; padding: 0 10px; font-size: 10px; letter-spacing: .3px;
    position: relative;
  }
  .toolbar::before {
    content: ""; position: absolute; top: -1px; left: 133px;
    border-left: 6px solid transparent; border-right: 6px solid transparent; border-top: 6px solid var(--tab-active);
  }
  .toolbar .dim { color: var(--text-dim); }
  .toolbar a { color: var(--text-light); text-decoration: underline; font-weight: 600; }
  .toolbar .divider { width: 1px; height: 18px; background: #555; margin: 0 10px; }
  .toolbar .center { position: absolute; left: 50%; transform: translateX(-50%); }
  .toolbar .right { margin-left: auto; display: flex; align-items: center; padding-right: 2px; }

  .pager { height: 40px; display: flex; align-items: center; font-size: 10px; color: var(--text-soft); gap: 4px; }
  .pager .pages { display: flex; gap: 4px; margin-right: 16px; }
  .pager .size { background: #fff; border: 1px solid #ccc; padding: 0 4px; margin: 0 4px; }

  table.grid { width: 1112px; border-collapse: collapse; table-layout: fixed; }
  .grid th {
    height: 41px; background: linear-gradient(#3c3c3c, #232323); color: #f2f2f2;
    font-size: 12px; font-weight: 400; border-right: 1px solid #4a4a4a;
  }
  .grid td {
    height: 41.5px; text-align: center; font-size: 12px; line-height: 14px; color: var(--text);
    background: linear-gradient(var(--row-top), var(--row-bottom));
    border-right: 1px solid #dadada; border-bottom: 1px solid var(--line); padding: 0 6px;
  }
  .grid th:last-child, .grid td:last-child { border-right: 0; }
  .pager.bottom { height: 38px; }
</style>
</head>
<body>
<div class="app">
  <header class="masthead">
    <div class="brand"><span class="brand-mark"></span>plume finder</div>
    <div class="search">
      <div class="search-field">search...</div>
      <div class="search-btn">
        <svg width="12" height="12" viewBox="0 0 12 12"><circle cx="5" cy="5" r="3.6" fill="none" stroke="#fff" stroke-width="1.6"/><line x1="7.6" y1="7.6" x2="11" y2="11" stroke="#fff" stroke-width="1.8"/></svg>
      </div>
      <div class="search-options">Search Options
        <span class="chev"><svg width="8" height="6" viewBox="0 0 8 6"><path d="M0 0h8L4 6z" fill="#333"/></svg></span>
      </div>
    </div>
  </header>

  <nav class="navbar">
    <div class="tab">Instructions</div>
    <div class="tab active">Student Data</div>
    <div class="user">Welcome, Owen <span class="sep">|</span> <a href="#">my profile</a> <span class="sep">|</span> <a href="#">log out</a></div>
  </nav>

  <div class="toolbar">
    <span class="dim">SHOWING 36 OF 48 COLUMNS</span><span class="divider"></span><a href="#">SHOW/HIDE COLUMNS</a>
    <span class="center"><span class="dim">3 COLUMNS ARE </span><a href="#">FILTERED</a></span>
    <span class="right"><a href="#">PRINT</a><span class="divider"></span><a href="#">DOWNLOAD</a></span>
  </div>

  <div class="pager"><span class="pages">◂ 1 2 3 4 5 ▸</span>show <span class="size">10</span> rows per page</div>

  <table class="grid">
    <thead>
      <tr><th>Date</th><th>Grade</th><th>ESC</th><th>CDC#</th><th>District</th><th>Campus</th><th>Last Name</th><th>First Name</th><th>MI</th><th>Student ID</th><th>Gender</th><th>DOB</th><th>Hisp</th></tr>
    </thead>
    <tbody>
      <tr><td>411</td><td>9</td><td>10</td><td>9999999901</td><td>Example District</td><td>Example HS</td><td>Accountability</td><td>Marisol</td><td>G</td><td>63054330</td><td>F</td><td>7311996</td><td>1</td></tr>
      <tr><td>411</td><td>9</td><td>10</td><td>9999999901</td><td>Example District</td><td>Example HS</td><td>Accountability</td><td>Marisol</td><td>G</td><td>63054330</td><td>F</td><td>7311996</td><td>1</td></tr>
      <tr><td>411</td><td>9</td><td>10</td><td>9999999901</td><td>Example District</td><td>Example HS</td><td>Accountability</td><td>Marisol</td><td>G</td><td>63054330</td><td>F</td><td>7311996</td><td>1</td></tr>
      <tr><td>411</td><td>9</td><td>10</td><td>9999999901</td><td>Example District</td><td>Example HS</td><td>Accountability</td><td>Marisol</td><td>G</td><td>63054330</td><td>F</td><td>7311996</td><td>1</td></tr>
      <tr><td>411</td><td>9</td><td>10</td><td>9999999901</td><td>Example District</td><td>Example HS</td><td>Accountability</td><td>Marisol</td><td>G</td><td>63054330</td><td>F</td><td>7311996</td><td>1</td></tr>
      <tr><td>411</td><td>9</td><td>10</td><td>9999999901</td><td>Example District</td><td>Example HS</td><td>Accountability</td><td>Marisol</td><td>G</td><td>63054330</td><td>F</td><td>7311996</td><td>1</td></tr>
      <tr><td>411</td><td>9</td><td>10</td><td>9999999901</td><td>Example District</td><td>Example HS</td><td>Accountability</td><td>Marisol</td><td>G</td><td>63054330</td><td>F</td><td>7311996</td><td>1</td></tr>
      <tr><td>411</td><td>9</td><td>10</td><td>9999999901</td><td>Example District</td><td>Example HS</td><td>Accountability</td><td>Marisol</td><td>G</td><td>63054330</td><td>F</td><td>7311996</td><td>1</td></tr>
    </tbody>
  </table>

  <div class="pager bottom"><span class="pages">◂ 1 2 3 4 5 ▸</span>show <span class="size">10</span> rows per page</div>
</div>
</body>
</html>
```